Stainless Steel Water Bottle Packaging

We need a design for our cylindrical water bottle packaging.

Please see attached template (500ml cola bottle template .ai file) for exact dimensions.

VORO is defined as the elemental forces of nature embodied in an object or person. The design should be eye catching and draw potential clients in. Although its a cylindrical bottle/box, the front which would face the customer when sitting on a shelf should clearly display our logo.

Industry/Entity Type

Steel

Requirements
Must have
• Designed to the specifications of the attached template (see attached)
• Our VORO Logo (see attached) and website www.vorobottle.example(in smaller font) must appear.
• Size of bottle must appear - '17 oz/500 ml'
• These should appear somewhere:
• 'INULATED DOUBLE-WALL STAINLESS STEEL WATER BOTTLE'
• 'VORO Bottles magically keeps drinks cold for up to 24hrs, hot for 12',
• 'BPA Free'
• 'For every VORO bottle purchased, a portion of proceeds will go towards charity. Each of our colour's have been assigned a specific charity. Please visit www.vorobottle.example to find out which charity you helped support!'
• The Top circle - just our Symbol (flame/drop)
• The bottom circle - 'Inc. Designed in Canada made in China' on the outer edge leaving the middle empty for the UPC code.
• Reference website for the bottle case I'm looking for:
• http://shopkorinday.example/t-flow-lagoon-pink-insulated-water-bottle
Nice to have
• illustration of our water bottle shape (see attached) appearing somewhere on the box is something i had in mind but definitely not necessary.

```html
<!DOCTYPE html>
<html lang="en">
<head>
<meta charset="utf-8">
<title>VORO Bottle Packaging</title>
<link href="https://fonts.googleapis.com/css2?family=Open+Sans:wght@400;600&family=Roboto+Condensed:wght@400&display=swap" rel="stylesheet">
<style>
  :root {
    --paper: #ffffff;
    --charcoal: #333333;
    --charcoal-deep: #242424;
    --charcoal-light: #404040;
    --wave-light: rgba(255,255,255,0.05);
    --wave-dark: rgba(0,0,0,0.18);
    --brand-blue: #2ea3d8;
    --brand-yellow: #f2bf22;
    --ink-light: #ffffff;
    --bottle-gold: #97782a;
    --bottle-stone: #a39a82;
    --bottle-teal: #2f6f8c;
    --flame-light: #fbe05a;
  }
  * { box-sizing: border-box; margin: 0; padding: 0; }
  html, body { width: 809px; height: 1200px; overflow: hidden; background: var(--paper); }
  .sheet { position: relative; width: 809px; height: 1200px; }

  /* dark panels with a soft layered tone in place of the wave texture */
  .panel {
    position: absolute;
    overflow: hidden;
    color: var(--ink-light);
    text-align: center;
    background:
      radial-gradient(ellipse 70% 30% at 20% 25%, var(--wave-light), transparent 70%),
      radial-gradient(ellipse 60% 25% at 80% 60%, var(--wave-light), transparent 70%),
      radial-gradient(ellipse 80% 30% at 50% 95%, var(--wave-dark), transparent 70%),
      linear-gradient(160deg, var(--charcoal-light) 0%, var(--charcoal) 55%, var(--charcoal-deep) 100%);
  }

  .lid { border-radius: 50%; width: 298px; height: 298px; top: 45px;
         display: flex; align-items: center; justify-content: center; }
  .lid--left { left: 76px; }
  .lid--right { left: 438px; }
  .lid .brand-name { position: static; font-size: 62px; color: var(--brand-yellow); }

  .band { top: 362px; width: 323px; height: 111px; }
  .band--left { left: 74px; }
  .band--right { left: 428px; }

  .wrap { top: 490px; width: 323px; height: 582px; }
  .wrap--left { left: 74px; }
  .wrap--right { left: 427px; }

  .brand-name {
    position: absolute; left: 0; right: 0;
    font-family: "Open Sans", sans-serif;
    font-weight: 600;
    color: var(--brand-blue);
    letter-spacing: 3px;
    line-height: 1;
  }
  .band .brand-name { top: 40px; font-size: 32px; }
  .wrap .brand-name { top: 358px; font-size: 32px; }

  .site {
    position: absolute; left: 0; right: 0;
    font-family: "Roboto Condensed", sans-serif;
    line-height: 1;
  }
  .band .site { top: 84px; font-size: 19px; }
  .band--right .site { top: 87px; font-family: "Open Sans", sans-serif; font-size: 11.5px; letter-spacing: 3.4px; color: var(--brand-yellow); }

  .hero { position: absolute; left: 81px; top: 25px; width: 160px; height: 307px; }
  .hero--bottle {
    border-radius: 70px 70px 40px 40px;
    background: linear-gradient(180deg, var(--bottle-gold) 0%, var(--bottle-stone) 50%, var(--bottle-teal) 100%);
    opacity: .85;
  }

  .hero-name {
    position: absolute; left: 0; right: 0; top: 148px;
    font-family: "Open Sans", sans-serif; font-weight: 600;
    font-size: 72px; letter-spacing: 3px; color: var(--flame-light); line-height: 1;
  }

  .product-lines {
    position: absolute; left: 0; right: 0; top: 422px;
    font-family: "Open Sans", sans-serif; font-size: 11px; line-height: 15px;
  }
  .product-lines span { display: block; letter-spacing: 3px; }
  .product-lines .lead { font-family: "Roboto Condensed", sans-serif; font-size: 12.5px; letter-spacing: 0; }

  .volume {
    position: absolute; left: 0; right: 0; top: 496px;
    font-family: "Roboto Condensed", sans-serif; font-size: 23px; line-height: 1;
  }
  .wrap--right .volume { font-family: "Open Sans", sans-serif; font-size: 20px; }

  .wrap .site { top: 556px; font-size: 15px; }
  .wrap--right .site { font-family: "Open Sans", sans-serif; font-size: 13px; color: var(--brand-blue); }
</style>
</head>
<body>
<main class="sheet">
  <section class="panel lid lid--left"><span class="brand-name">VORO</span></section>
  <section class="panel lid lid--right"><span class="brand-name">VORO</span></section>

  <section class="panel band band--left">
    <div class="brand-name">VORO</div>
    <div class="site">www.vorobottle.example</div>
  </section>
  <section class="panel band band--right">
    <div class="brand-name">VORO</div>
    <div class="site">www.vorobottle.example</div>
  </section>

  <section class="panel wrap wrap--left">
    <div class="hero hero--bottle" role="img" aria-label="Illustration of the steel water bottle over a translucent flame and drop"></div>
    <div class="brand-name">VORO</div>
    <div class="product-lines">
      <span class="lead">INULATED DOUBLE-WALL</span>
      <span>STAINLESS STEEL</span>
      <span>WATER BOTTLE</span>
    </div>
    <div class="volume">17 oz/500 ml</div>
    <div class="site">www.vorobottle.example</div>
  </section>

  <section class="panel wrap wrap--right">
    <div class="hero-name">VORO</div>
    <div class="brand-name">VORO</div>
    <div class="product-lines">
      <span class="lead">INULATED DOUBLE-WALL</span>
      <span>STAINLESS STEEL</span>
      <span>WATER BOTTLE</span>
    </div>
    <div class="volume">17 oz/500 ml</div>
    <div class="site">www.vorobottle.example</div>
  </section>
</main>
</body>
</html>
```